Business Card Design

We do Metal Roofing, fascia and gutter and edge protection [safety rail].

Industry/Entity Type

Business

Contact Information for Business Card

Tarnwell Roof Plumbing. Metal Roofing, Fascia and Gutter, Edge Protection
Colin 0468305172
Finn 0419587364
tr7win5@mailvane.com
Lic: 614903K
ABN:52716340951

```html
<!DOCTYPE html>
<html lang="en">
<head>
<meta charset="utf-8">
<title>Tarnwell Roof Plumbing – Business Card</title>
<link rel="stylesheet" href="https://fonts.googleapis.com/css2?family=Montserrat:wght@400;500;700&display=swap">
<style>
  :root {
    --navy: #1a3d8f;
    --grey-text: #7b8086;
    --grey-bar: #8c9196;
    --card: #ffffff;
    --backdrop: #e9ebee;
  }
  * { margin: 0; padding: 0; box-sizing: border-box; }
  html, body {
    width: 1200px;
    height: 970px;
    overflow: hidden;
    background: var(--backdrop);
    font-family: "Montserrat", Arial, sans-serif;
  }
  .business-card {
    position: absolute;
    left: 100px;
    top: 207px;
    width: 1000px;
    height: 556px;
    background: var(--card);
    border: 1px solid #d6d9dd;
    box-shadow: 0 10px 30px rgba(0,0,0,0.08);
    overflow: hidden;
  }
  .contact { position: absolute; left: 58px; white-space: nowrap; }
  .contact-name {
    font-weight: 700;
    font-size: 29px;
    color: var(--navy);
    line-height: 34px;
  }
  .contact-line {
    display: flex;
    align-items: center;
    gap: 10px;
    font-size: 25px;
    color: var(--grey-text);
    line-height: 30px;
    letter-spacing: 0.3px;
  }
  .contact-line svg { flex: none; fill: var(--grey-text); }
  .reg-label { font-weight: 700; color: var(--navy); margin-right: 8px; }
  .name-colin { top: 108px; }
  .phone-colin { top: 147px; }
  .name-finn { top: 206px; }
  .phone-finn { top: 247px; }
  .licence { top: 321px; }
  .abn { top: 362px; }
  .email { top: 418px; }

  .company-name {
    position: absolute;
    left: 513px;
    top: 100px;
    width: 430px;
    color: var(--navy);
    font-weight: 700;
    text-align: center;
    line-height: 1;
    white-space: nowrap;
  }
  .company-name .primary { display: block; font-size: 68px; letter-spacing: 0; }
  .company-name .secondary { display: block; font-size: 44px; margin-top: 44px; letter-spacing: 0.3px; }

  .services {
    position: absolute;
    left: 526px;
    top: 340px;
    list-style: none;
  }
  .services li {
    display: flex;
    align-items: center;
    gap: 12px;
    font-size: 25px;
    color: var(--grey-text);
    line-height: 34px;
    letter-spacing: 0.3px;
    white-space: nowrap;
  }
  .services svg { flex: none; }

  .band { position: absolute; top: 521px; height: 35px; }
  .band-left { left: 0; width: 503px; background: var(--grey-bar); opacity: 0.75; }
  .band-right { left: 514px; right: 0; background: var(--navy); }
</style>
</head>
<body>
  <div class="business-card">
    <div class="contact contact-name name-colin">Colin</div>
    <div class="contact contact-line phone-colin">
      <svg width="20" height="20" viewBox="0 0 24 24" aria-hidden="true"><path d="M6.6 10.8c1.4 2.8 3.8 5.1 6.6 6.6l2.2-2.2c.3-.3.7-.4 1-.2 1.1.4 2.3.6 3.6.6.6 0 1 .4 1 1V20c0 .6-.4 1-1 1C10.6 21 3 13.4 3 4c0-.6.4-1 1-1h3.5c.6 0 1 .4 1 1 0 1.3.2 2.5.6 3.6.1.3 0 .7-.2 1l-2.3 2.2z"/></svg>
      <span>0468305172</span>
    </div>
    <div class="contact contact-name name-finn">Finn</div>
    <div class="contact contact-line phone-finn">
      <svg width="20" height="20" viewBox="0 0 24 24" aria-hidden="true"><path d="M6.6 10.8c1.4 2.8 3.8 5.1 6.6 6.6l2.2-2.2c.3-.3.7-.4 1-.2 1.1.4 2.3.6 3.6.6.6 0 1 .4 1 1V20c0 .6-.4 1-1 1C10.6 21 3 13.4 3 4c0-.6.4-1 1-1h3.5c.6 0 1 .4 1 1 0 1.3.2 2.5.6 3.6.1.3 0 .7-.2 1l-2.3 2.2z"/></svg>
      <span>0419587364</span>
    </div>
    <div class="contact contact-line licence"><span class="reg-label">Lic #</span>614903K</div>
    <div class="contact contact-line abn"><span class="reg-label">ABN #</span>52716340951</div>
    <div class="contact contact-line email">
      <svg width="22" height="16" viewBox="0 0 22 16" aria-hidden="true"><path d="M0 1.5 11 9 22 1.5V16H0z"/><path d="M0 0h22L11 7.4z"/></svg>
      <span>tr7win5@mailvane.com</span>
    </div>

    <div class="company-name">
      <span class="primary">TARNWELL</span>
      <span class="secondary">ROOF PLUMBING</span>
    </div>

    <ul class="services">
      <li><svg width="22" height="22" viewBox="0 0 22 22" aria-hidden="true"><rect x="1.5" y="3.5" width="16" height="16" fill="none" stroke="#1a3d8f" stroke-width="2.5"/><path d="M5 10.5l4 4L20.5 2" fill="none" stroke="#1a3d8f" stroke-width="3"/></svg>Metal Roofing</li>
      <li><svg width="22" height="22" viewBox="0 0 22 22" aria-hidden="true"><rect x="1.5" y="3.5" width="16" height="16" fill="none" stroke="#1a3d8f" stroke-width="2.5"/><path d="M5 10.5l4 4L20.5 2" fill="none" stroke="#1a3d8f" stroke-width="3"/></svg>Fascia</li>
      <li><svg width="22" height="22" viewBox="0 0 22 22" aria-hidden="true"><rect x="1.5" y="3.5" width="16" height="16" fill="none" stroke="#1a3d8f" stroke-width="2.5"/><path d="M5 10.5l4 4L20.5 2" fill="none" stroke="#1a3d8f" stroke-width="3"/></svg>Gutter</li>
      <li><svg width="22" height="22" viewBox="0 0 22 22" aria-hidden="true"><rect x="1.5" y="3.5" width="16" height="16" fill="none" stroke="#1a3d8f" stroke-width="2.5"/><path d="M5 10.5l4 4L20.5 2" fill="none" stroke="#1a3d8f" stroke-width="3"/></svg>Edge Protection</li>
    </ul>

    <div class="band band-left"></div>
    <div class="band band-right"></div>
  </div>
</body>
</html>
```